Dog grooming business card
This is a business card for m dog grooming business like it say above.
In the priorities box below I will have the text that I want on the card.

Industry/Entity Type

Business

Colors

Designer to choose colors to be used in the design.

Requirements
Must have
• My logo and the insurance stamp must be on the card.

Text it must have :

Professional grooming services
Email: lunabrisk@mailvane.net
Text or call 1 705 318 6642
TKV certified/member
Pet first aid certified
Next appointment ___________________________________
Nice to have
• Greens to match my logo

```html
<!DOCTYPE html>
<html lang="en">
<head>
<meta charset="utf-8">
<title>Luna Brisk – Grooming Business Card</title>
<link href="https://fonts.googleapis.com/css2?family=Arimo:wght@400;700&display=swap" rel="stylesheet">
<style>
  :root {
    --page-bg: #5d6169;
    --card-dark: #17121a;
    --card-light: #ffffff;
    --brand-green: #8cc63f;
    --ink: #1a1a1a;
    --badge-blue: #2e7fd0;
  }
  html, body {
    margin: 0;
    padding: 0;
    width: 1200px;
    height: 960px;
    overflow: hidden;
    background: var(--page-bg);
    font-family: "Arimo", Arial, sans-serif;
  }
  .stage {
    position: relative;
    width: 1200px;
    height: 960px;
  }
  .card {
    position: absolute;
    left: 260px;
    width: 680px;
    height: 389px;
    border-radius: 22px;
    box-shadow: 0 10px 30px rgba(0,0,0,0.35);
    overflow: hidden;
  }
  .card-front {
    top: 70px;
    background: var(--card-dark);
    display: flex;
    align-items: center;
    justify-content: center;
  }
  .brand-lockup {
    display: flex;
    align-items: center;
    gap: 16px;
  }
  .brand-dot {
    width: 34px;
    height: 34px;
    border-radius: 50%;
    background: var(--brand-green);
  }
  .brand-name {
    font-size: 46px;
    font-weight: 700;
    color: var(--brand-green);
    letter-spacing: 0.5px;
  }
  .card-back {
    top: 500px;
    background: var(--card-light);
  }
  .tagline {
    position: absolute;
    left: 70px;
    top: 52px;
    margin: 0;
    font-size: 30px;
    font-weight: 700;
    color: var(--brand-green);
  }
  .credentials {
    position: absolute;
    left: 200px;
    top: 118px;
    margin: 0;
    font-size: 19px;
    font-weight: 700;
    line-height: 1.3;
    color: var(--ink);
  }
  .credentials span { display: block; }
  .credentials .indent { padding-left: 22px; font-weight: 400; }
  .next-appointment {
    position: absolute;
    left: 260px;
    top: 192px;
    margin: 0;
    font-size: 17px;
    color: var(--brand-green);
  }
  .appointment-line {
    position: absolute;
    left: 70px;
    right: 70px;
    top: 236px;
    border-top: 3px dotted var(--ink);
  }
  .contact {
    position: absolute;
    left: 70px;
    top: 258px;
    margin: 0;
    font-size: 18px;
    color: var(--ink);
    white-space: nowrap;
  }
  .contact .accent { color: var(--brand-green); }
  .insurance-badge {
    position: absolute;
    left: 300px;
    top: 300px;
  }
</style>
</head>
<body>
<main class="stage">
  <section class="card card-front" aria-label="Card front">
    <div class="brand-lockup">
      <span class="brand-dot"></span>
      <span class="brand-name">Luna Brisk</span>
    </div>
  </section>

  <section class="card card-back" aria-label="Card back">
    <h1 class="tagline">Professional grooming services</h1>
    <p class="credentials">
      <span>TKV certified/member</span>
      <span class="indent">Pet first aid certified</span>
    </p>
    <p class="next-appointment">Next appointment</p>
    <div class="appointment-line"></div>
    <p class="contact">lunabrisk@mailvane.net <span class="accent">Text</span> or <span class="accent">call</span> 1 705 318 6642</p>
    <svg class="insurance-badge" width="100" height="56" viewBox="0 0 100 56" role="img" aria-label="Insurance stamp">
      <rect x="2" y="2" width="96" height="52" rx="8" fill="#ffffff" stroke="var(--badge-blue)" stroke-width="2.5"/>
    </svg>
  </section>
</main>
</body>
</html>
```